Innovative IT Service Provider seeks engaging overview presentation to capture new business

*Please see attached Creative Brief for full details*

Overall Goals
The goal of this presentation is to provide new, prospective clients with an introduction to Harborline Systems, the services we provide, and what makes us a unique and superior choice for their IT Services. The deck should be able to clearly relay this information while clients review it on their own, without further explanation from a company representative.

Design Goals
We are looking for a professional, modern, streamlined, sleek design that reflects our status as a leader in information technology and innovation.

Company Overview
As an IT Managed Service Provider, companies choose to outsource some or all of their internal IT functions to us to take advantage of our many areas of expertise and so they can focus on their core business, whatever industry they may be in. We also specialize in IT Cyber Security and Consulting, always providing our clients with thought leadership and insight into the latest IT innovations. We ultimately find ways to deliver value to our clients through our various IT solutions.

```html
<!DOCTYPE html>
<html lang="en">
<head>
<meta charset="utf-8">
<title>Harborline Systems — Presentation Overview</title>
<link href="https://fonts.googleapis.com/css2?family=Open+Sans:wght@400;600;700&display=swap" rel="stylesheet">
<style>
:root{
  --bg:#eef2fa;
  --navy:#1d3763;
  --navy-deep:#0e1b36;
  --night:#05070d;
  --red:#c8102e;
  --ink:#1b1d22;
  --grey:#8b909a;
  --soft:#c7ccd6;
  --line:#dfe3ea;
  --white:#ffffff;
}
*{box-sizing:border-box;margin:0;padding:0}
html,body{width:1200px;height:966px;overflow:hidden}
body{background:var(--bg);position:relative;font-family:'Open Sans',sans-serif;color:var(--ink)}
.slide{position:absolute;width:447px;height:248px;transform:scale(.5568);transform-origin:0 0;background:var(--white);overflow:hidden;box-shadow:0 22px 34px rgba(25,45,90,.16)}
.a{position:absolute}
.center{left:0;right:0;text-align:center}
.red{color:var(--red)}
.navy-t{color:var(--navy)}
.dark{background:var(--navy-deep);color:var(--white)}
.photo{position:absolute}
.brand-mark{font-size:5px;font-weight:700;letter-spacing:.6px;display:flex;align-items:center;justify-content:center;gap:3px;color:var(--navy)}
.brand-mark::before{content:"";width:6px;height:6px;background:currentColor}
.dark .brand-mark{color:var(--white)}
.brand-left{justify-content:flex-start}
.cover-title{font-size:14.5px;font-weight:700}
.cover-sub{font-size:7px;color:#c5cbd8}
.light .cover-sub{color:#333}
.presenter{font-size:8px;font-weight:700}
.light .presenter{color:var(--navy)}
.date,.domain{font-size:5px;color:#c5cbd8}
.light .date,.light .domain{color:#555}
.footer{position:absolute;left:0;right:0;bottom:0;height:11px;background:var(--navy);color:var(--white);font-size:5px;display:grid;grid-template-columns:1fr 1fr 1fr;align-items:center;padding:0 10px}
.footer .brand-mark{color:var(--white);font-size:4px;justify-content:flex-start}
.footer .f-site{text-align:center}
.footer .f-page{text-align:right}
.accent{position:absolute;width:12px;height:1.3px;background:var(--red)}
.title{font-size:14px;font-weight:700;color:var(--ink)}
.sub{font-size:3.6px;color:var(--grey)}
.body{font-size:3.6px;line-height:1.55;color:#6a707b}
.list-row{position:absolute;width:133px;border-bottom:1px solid #333;font-size:4.4px;font-weight:600;display:flex;justify-content:space-between;padding-bottom:3px}
.list-row.active{border-bottom-color:var(--red);color:var(--navy)}
.card{position:absolute;background:var(--white);box-shadow:0 3px 10px rgba(20,40,80,.12)}
.card.fill{background:var(--navy);color:var(--white)}
.card.fill .body{color:#c9d2e4}
.stat{font-size:10px;font-weight:600;text-align:center}
.stat-label{font-size:3.6px;text-align:center;color:#555}
.card.fill .stat-label{color:#dbe2f0}
.cell-head{font-size:4.4px;font-weight:700;color:var(--navy);text-align:center}
.dash{width:5px;height:1px;background:var(--red);margin:3px auto}
.icon{display:block;margin:0 auto}
.swot-col{position:absolute;width:92px;padding:8px 6px;font-size:3.4px;line-height:1.9;color:#555}
.swot-col h4{font-size:5px;font-weight:400;color:#333;margin-bottom:3px}
.swot-col.fill{background:var(--navy);color:#dbe2f0}
.swot-col.fill h4{color:var(--white)}
.step-head{font-size:5px;font-weight:600;color:#333;margin-bottom:2px}
.kpi{font-size:9px;font-weight:700;color:var(--navy);text-align:center}
.kpi-label{font-size:3.4px;font-weight:700;text-align:center;color:var(--navy)}
.dash-title{font-size:7.5px;font-weight:700;color:var(--navy)}
</style>
</head>
<body>

<!-- Row 1 -->
<section class="slide dark" style="left:43px;top:39px">
  <div class="photo" style="inset:0;background:linear-gradient(120deg,#1c2a4a,#0c1730 60%,#16223c)" role="img" aria-label="Dimmed photo of a laptop workspace on a desk"></div>
  <div class="brand-mark a center" style="top:36px">HARBORLINE SYSTEMS</div>
  <h1 class="cover-title a center" style="top:108px">Presentation Title Goes Here</h1>
  <p class="cover-sub a center" style="top:134px">Credential Subtitle Presentation</p>
  <p class="presenter a center" style="top:172px">Mr. Adam <span class="red">Rowley</span></p>
  <p class="date a" style="left:21px;top:225px">August <span class="red">2023</span></p>
  <p class="domain a" style="right:21px;top:225px">harborlinesys.com</p>
</section>

<section class="slide dark" style="left:330px;top:39px">
  <div class="photo" style="inset:0;background:linear-gradient(110deg,#0f1a33,#1a2747)" role="img" aria-label="Dimmed photo of hands typing on a laptop"></div>
  <div class="photo" style="left:215px;top:20px;width:215px;height:200px;background:linear-gradient(135deg,#56617a,#b8a48e 50%,#3b4763)" role="img" aria-label="Photo of a laptop keyboard and office scene"></div>
  <div class="brand-mark a brand-left" style="left:22px;top:42px">HARBORLINE SYSTEMS</div>
  <h1 class="cover-title a" style="left:22px;top:100px">Presentation Title Goes Here</h1>
  <p class="cover-sub a" style="left:22px;top:124px">Credential Subtitle Presentation</p>
  <p class="presenter a" style="left:22px;top:160px">Mr. Adam <span class="red">Rowley</span></p>
  <p class="date a" style="left:22px;top:225px">August <span class="red">2023</span></p>
</section>

<section class="slide light" style="left:617.5px;top:39px">
  <div class="brand-mark a center" style="top:36px">HARBORLINE SYSTEMS</div>
  <h1 class="cover-title a center" style="top:108px;color:var(--ink)">Presentation Title Here</h1>
  <p class="cover-sub a center" style="top:134px">Credential Subtitle Presentation</p>
  <p class="presenter a center" style="top:172px">Mr. Adam <span class="red">Rowley</span></p>
  <p class="date a" style="left:21px;top:225px">August <span class="red">2023</span></p>
  <p class="domain a" style="right:21px;top:225px">harborlinesys.com</p>
</section>

<section class="slide light" style="left:905px;top:39px">
  <div class="photo" style="left:225px;top:20px;width:205px;height:190px;background:linear-gradient(135deg,#e9ecf1,#c9c2ba 50%,#8c93a0)" role="img" aria-label="Photo of a laptop on a bright desk"></div>
  <div class="brand-mark a brand-left" style="left:21px;top:38px">HARBORLINE SYSTEMS</div>
  <h1 class="cover-title a" style="left:21px;top:108px;color:var(--ink)">Presentation Title Here</h1>
  <p class="cover-sub a" style="left:21px;top:134px">Credential Subtitle Presentation</p>
  <p class="presenter a" style="left:21px;top:172px">Mr. Adam <span class="red">Rowley</span></p>
  <p class="date a" style="left:21px;top:225px">August <span class="red">2023</span></p>
  <p class="domain a" style="right:21px;top:225px">harborlinesys.com</p>
</section>

<!-- Row 2 -->
<section class="slide" style="left:43px;top:225.5px">
  <div class="accent" style="left:217px;top:20px"></div>
  <h2 class="title a center" style="top:26px">Presentation List</h2>
  <p class="sub a center" style="top:46px">Here Our Subtitle</p>
  <div class="list-row" style="left:60px;top:80px"><span>COVER SLIDES</span><span>01</span></div>
  <div class="list-row active" style="left:60px;top:112px"><span>PRESENTATION LIST</span><span>03</span></div>
  <div class="list-row" style="left:60px;top:144px"><span>ABOUT US</span><span>04</span></div>
  <div class="list-row" style="left:60px;top:176px"><span>OUR MISSIONS &amp; VISION</span><span>06</span></div>
  <div class="list-row" style="left:254px;top:80px"><span>INFOGRAPH ONE</span><span>07</span></div>
  <div class="list-row" style="left:254px;top:112px"><span>INFOGRAPH TWO</span><span>08</span></div>
  <div class="list-row" style="left:254px;top:144px"><span>INFOGRAPH THREE</span><span>09</span></div>
  <div class="list-row" style="left:254px;top:176px"><span>CLOSING SLIDES</span><span>10</span></div>
  <div class="footer"><span class="brand-mark">HARBORLINE SYSTEMS</span><span class="f-site">harborlinesys.com</span><span class="f-page">page | 5</span></div>
</section>

<section class="slide" style="left:330px;top:225.5px">
  <div class="accent" style="left:217px;top:20px"></div>
  <h2 class="title a center" style="top:26px">Our Vision</h2>
  <p class="sub a center" style="top:46px">Here Our Subtitle</p>
  <div class="card fill" style="left:56px;top:73px;width:335px;height:116px;display:flex;align-items:center;justify-content:center;padding:0 36px">
    <p style="font-size:6.2px;line-height:1.75;text-align:center">Lorem ipsum dolor sit amet, consectetuer adipiscing elit. Maecenas porttitor congue massa. Fusce posuere, magna sed pulvinar ultricies, purus lectus malesuada libero.</p>
  </div>
  <div class="footer"><span class="brand-mark">HARBORLINE SYSTEMS</span><span class="f-site">harborlinesys.com</span><span class="f-page">page | 6</span></div>
</section>

<section class="slide" style="left:617.5px;top:225.5px">
  <div class="accent" style="left:217px;top:18px"></div>
  <h2 class="title a center" style="top:24px">Our Mission</h2>
  <div class="card" style="left:168px;top:70px;width:110px;height:68px"></div>
  <div class="a" style="left:35px;top:77px;width:105px"><p class="cell-head">Mission One</p><div class="dash"></div><p class="body" style="text-align:center">Lorem ipsum dolor sit amet, consecter adipiscing eli Maecenas porttitor adipiscing elit tam emotan.</p></div>
  <div class="a" style="left:171px;top:77px;width:105px"><p class="cell-head">Mission Two</p><div class="dash"></div><p class="body" style="text-align:center">Lorem ipsum dolor sit amet, consecter adipiscing eli Maecenas porttitor adipiscing elit tam emotan.</p></div>
  <div class="a" style="left:307px;top:77px;width:105px"><p class="cell-head">Mission Three</p><div class="dash"></div><p class="body" style="text-align:center">Lorem ipsum dolor sit amet, consecter adipiscing eli Maecenas porttitor adipiscing elit tam emotan.</p></div>
  <div class="a" style="left:35px;top:154px;width:105px"><p class="cell-head">Mission Four</p><div class="dash"></div><p class="body" style="text-align:center">Lorem ipsum dolor sit amet, consecter adipiscing eli Maecenas porttitor adipiscing elit tam emotan.</p></div>
  <div class="a" style="left:171px;top:154px;width:105px"><p class="cell-head">Mission Five</p><div class="dash"></div><p class="body" style="text-align:center">Lorem ipsum dolor sit amet, consecter adipiscing eli Maecenas porttitor adipiscing elit tam emotan.</p></div>
  <div class="a" style="left:307px;top:154px;width:105px"><p class="cell-head">Mission Six</p><div class="dash"></div><p class="body" style="text-align:center">Lorem ipsum dolor sit amet, consecter adipiscing eli Maecenas porttitor adipiscing elit tam emotan.</p></div>
  <div class="footer"><span class="brand-mark">HARBORLINE SYSTEMS</span><span class="f-site">harborlinesys.com</span><span class="f-page">page | 7</span></div>
</section>

<section class="slide" style="left:905px;top:225.5px">
  <div class="accent" style="left:217px;top:24px"></div>
  <h2 class="title a center" style="top:32px">About HS</h2>
  <div class="accent" style="left:220px;top:53px;width:6px"></div>
  <p class="body a center" style="top:82px;padding:0 55px"><b class="navy-t">Lorem ipsum</b> dolor sit amet, consectetuer adipiscing elit. Maecenas porttitor congue massa. Fusce posuere, magna sed pulvinar ultricies, purus lectus malesuada libero, sit amet commodo magna eros quis urna. Vivamus a tellus. Pellentesque habitant morbi tristique senectus et netus et malesuada.</p>
  <div class="card" style="left:32px;top:135px;width:84px;height:55px;padding-top:8px"><p class="stat">25+</p><div class="dash"></div><p class="stat-label">IT Management Solutions<br>Expertise</p></div>
  <div class="card fill" style="left:129px;top:135px;width:90px;height:55px;padding-top:8px"><p class="stat">80K</p><div class="dash"></div><p class="stat-label">Devices under management<br>Globally</p></div>
  <div class="card" style="left:231px;top:135px;width:84px;height:55px;padding-top:8px"><p class="stat">7500+</p><div class="dash"></div><p class="stat-label">Service Desk<br>handles</p></div>
  <div class="card" style="left:327px;top:135px;width:84px;height:55px;padding-top:8px"><p class="stat">500</p><div class="dash"></div><p class="stat-label">Partner to<br>Fortune</p></div>
  <div class="footer"><span class="brand-mark">HARBORLINE SYSTEMS</span><span class="f-site">harborlinesys.com</span><span class="f-page">page | 8</span></div>
</section>

<!-- Row 3 -->
<section class="slide" style="left:43px;top:412px">
  <div class="photo" style="left:47px;top:63px;width:118px;height:107px;background:linear-gradient(135deg,#9fb4c4,#5d7688 55%,#2e3d4c)" role="img" aria-label="Photo of a businessman reading on a sofa by a city window"></div>
  <div class="accent" style="left:203px;top:64px"></div>
  <h2 class="a" style="left:203px;top:70px;font-size:12px;font-weight:700">About Harborline Systems</h2>
  <p class="body a" style="left:203px;top:93px;width:200px">Lorem ipsum dolor sit amet, consectetuer adipiscing elit. Maecenas porttitor congue massa. Fusce posuere, magna sed pulvinar ultricies.</p>
  <div class="card" style="left:205px;top:126px;width:46px;height:44px;padding-top:12px"><p class="stat" style="font-size:7px">12+</p><p class="stat-label" style="font-size:3px">Partnership</p></div>
  <div class="card fill" style="left:250px;top:124px;width:54px;height:48px;padding-top:13px"><p class="stat" style="font-size:7px">870+</p><p class="stat-label" style="font-size:3px">Satisfy Customer</p></div>
  <div class="card" style="left:304px;top:126px;width:46px;height:44px;padding-top:12px"><p class="stat" style="font-size:7px">200+</p><p class="stat-label" style="font-size:3px">Employee</p></div>
  <div class="footer"><span class="brand-mark">HARBORLINE SYSTEMS</span><span class="f-site">harborlinesys.com</span><span class="f-page">page | 9</span></div>
</section>

<section class="slide" style="left:330px;top:412px;background:var(--night);color:var(--white)">
  <div class="photo" style="inset:0;background:radial-gradient(circle at 30% 40%,#12304a,#05070d 70%)" role="img" aria-label="Dark background photo with soft teal light points"></div>
  <div class="accent" style="left:32px;top:40px"></div>
  <h2 class="a" style="left:32px;top:44px;font-size:12.5px;font-weight:700">Our Featured</h2>
  <p class="a" style="left:32px;top:70px;width:120px;font-size:3.6px;line-height:1.75;color:#b9c0cc"><b style="color:#fff">Lorem ipsum</b> dolor sit amet, consectetuer adipiscing elit. Maecenas porttitor congue massa. Fusce posuere, magna sed pulvinar ultricies, purus lectus malesuada libero, sit amet commodo magna eros quis urna. Nunc viverra imperdiet enim. Fusce est.</p>
  <div class="a" style="left:225px;top:86px;width:190px;height:30px;background:rgba(255,255,255,.06)"></div>
  <svg class="a" style="left:236px;top:45px" width="16" height="160" viewBox="0 0 16 160">
    <circle cx="8" cy="9" r="6" fill="#2d5aa8"/><circle cx="8" cy="55" r="6" fill="#2d5aa8"/><circle cx="8" cy="101" r="6" fill="#2d5aa8"/><circle cx="8" cy="139" r="6" fill="#2d5aa8"/>
    <g fill="none" stroke="#fff" stroke-width="1"><path d="M5 9h6M8 6v6"/><path d="M5 55h6M8 52v6"/><path d="M5 101h6M8 98v6"/><path d="M5 139h6M8 136v6"/></g>
  </svg>
  <div class="a" style="left:255px;top:42px;width:150px;font-size:3.4px;line-height:1.7;color:#b9c0cc"><b style="color:#fff">Preparation</b><br>Business Enhancement Plans then Growth Strategy is one of the development with super team.</div>
  <div class="a" style="left:257px;top:88px;width:150px;font-size:3.4px;line-height:1.7;color:#b9c0cc"><b style="color:#fff">Mapping Market</b><br>Business Enhancement Plans then Growth Strategy is one of the development with super team.</div>
  <div class="a" style="left:255px;top:134px;width:150px;font-size:3.4px;line-height:1.7;color:#b9c0cc"><b style="color:#fff">Research &amp; Development</b><br>Business Enhancement Plans then Growth Strategy is one of the development with super team.</div>
  <div class="a" style="left:255px;top:172px;width:150px;font-size:3.4px;line-height:1.7;color:#b9c0cc"><b style="color:#fff">Execution</b><br>Business Enhancement Plans then Growth Strategy is one of the development with super team.</div>
  <div class="footer"><span class="brand-mark">HARBORLINE SYSTEMS</span><span class="f-site">harborlinesys.com</span><span class="f-page">page | 10</span></div>
</section>

<section class="slide" style="left:617.5px;top:412px">
  <div class="accent" style="left:217px;top:10px"></div>
  <h2 class="title a center" style="top:15px">Our Expertise</h2>
  <div class="card" style="left:43px;top:58px;width:70px;height:64px;padding-top:12px"><svg class="icon" width="14" height="12" viewBox="0 0 14 12"><g fill="none" stroke="var(--navy)" stroke-width=".8"><circle cx="4" cy="3" r="2"/><circle cx="10" cy="3" r="2"/><path d="M1 11c0-3 6-3 6 0M7 11c0-3 6-3 6 0"/></g></svg><div class="dash"></div><p class="cell-head" style="font-size:3.8px">Non-Profit</p></div>
  <div class="card" style="left:140px;top:58px;width:70px;height:64px;padding-top:12px"><svg class="icon" width="14" height="12" viewBox="0 0 14 12"><g fill="none" stroke="var(--navy)" stroke-width=".8"><rect x="1" y="3" width="8" height="6"/><path d="M9 5h3l1 2v2H9"/><circle cx="4" cy="10" r="1.2"/><circle cx="11" cy="10" r="1.2"/></g></svg><div class="dash"></div><p class="cell-head" style="font-size:3.8px">Transportation &amp;<br>Logistics</p></div>
  <div class="card" style="left:238px;top:58px;width:70px;height:64px;padding-top:12px"><svg class="icon" width="14" height="12" viewBox="0 0 14 12"><g fill="none" stroke="var(--navy)" stroke-width=".8"><circle cx="7" cy="4" r="3"/><path d="M2 11l3-3h5"/></g></svg><div class="dash"></div><p class="cell-head" style="font-size:3.8px">Financial &amp;<br>Banking</p></div>
  <div class="card" style="left:335px;top:58px;width:70px;height:64px;padding-top:12px"><svg class="icon" width="14" height="12" viewBox="0 0 14 12"><g fill="none" stroke="var(--navy)" stroke-width=".8"><path d="M7 1l5 2v3c0 3-2 5-5 6-3-1-5-3-5-6V3z"/><path d="M5 6l1.5 1.5L9 5"/></g></svg><div class="dash"></div><p class="cell-head" style="font-size:3.8px">Insurance</p></div>
  <div class="card" style="left:43px;top:136px;width:70px;height:64px;padding-top:12px"><svg class="icon" width="14" height="12" viewBox="0 0 14 12"><g fill="none" stroke="var(--navy)" stroke-width=".8"><path d="M7 11S2 8 2 4.5A2.5 2.5 0 0 1 7 3a2.5 2.5 0 0 1 5 1.5C12 8 7 11 7 11z"/></g></svg><div class="dash"></div><p class="cell-head" style="font-size:3.8px">Healthcare</p></div>
  <div class="card" style="left:140px;top:136px;width:70px;height:64px;padding-top:12px"><svg class="icon" width="14" height="12" viewBox="0 0 14 12"><g fill="none" stroke="var(--navy)" stroke-width=".8"><path d="M1 11V5l4 2V5l4 2V2h3v9z"/></g></svg><div class="dash"></div><p class="cell-head" style="font-size:3.8px">Manufacturing</p></div>
  <div class="card" style="left:238px;top:136px;width:70px;height:64px;padding-top:12px"><svg class="icon" width="14" height="12" viewBox="0 0 14 12"><g fill="none" stroke="var(--navy)" stroke-width=".8"><path d="M2 11V5l5-4 5 4v6z"/><rect x="5.5" y="7" width="3" height="4"/></g></svg><div class="dash"></div><p class="cell-head" style="font-size:3.8px">Real Estate</p></div>
  <div class="card" style="left:335px;top:136px;width:70px;height:64px;padding-top:12px"><svg class="icon" width="14" height="12" viewBox="0 0 14 12"><g fill="none" stroke="var(--navy)" stroke-width=".8"><rect x="2" y="1" width="4" height="4"/><rect x="8" y="1" width="4" height="4"/><rect x="2" y="7" width="4" height="4"/><path d="M10 7v4M8 9h4"/></g></svg><div class="dash"></div><p class="cell-head" style="font-size:3.8px">And More</p></div>
  <div class="footer"><span class="brand-mark">HARBORLINE SYSTEMS</span><span class="f-site">harborlinesys.com</span><span class="f-page">page | 11</span></div>
</section>

<section class="slide" style="left:905px;top:412px">
  <div class="accent" style="left:201px;top:20px;width:11px"></div>
  <h2 class="a center" style="top:25px;font-size:12.5px;font-weight:600">S.W.O.T Analayse</h2>
  <p class="body a center" style="top:82px;padding:0 60px"><b class="navy-t">Lorem ipsum</b> dolor sit amet, consectetuer adipiscing elit. Maecenas porttitor congue massa. Fusce posuere, magna sed pulvinar ultricies, sit amet commodo magna eros quis urna.</p>
  <div class="swot-col" style="left:26px;top:128px"><h4>Strenght</h4>1. Business Enhancement Plan<br>2. Growth Strategy is one<br>3. Way to development it self<br>4. With Super-team together</div>
  <div class="swot-col fill" style="left:127px;top:128px;height:70px"><h4>Weakness</h4>1. Business Enhancement Plan<br>2. Growth Strategy is ones<br>3. Way to development it self<br>4. With Super-team together</div>
  <div class="swot-col" style="left:226px;top:128px"><h4>Opportunity</h4>1. Ways to develop it self<br>2. Business Enhancement Plan<br>3. Growth Strategy is one<br>4. With Super-team together</div>
  <div class="swot-col" style="left:325px;top:128px"><h4>Thread</h4>1. Business Enhancement Plan<br>2. Growth Strategy is one<br>3. Ways to develop it self<br>4. With Super-team together</div>
  <div class="footer"><span class="brand-mark">HARBORLINE SYSTEMS</span><span class="f-site">harborlinesys.com</span><span class="f-page">page | 12</span></div>
</section>

<!-- Row 4 -->
<section class="slide" style="left:43px;top:598.5px">
  <div class="accent" style="left:217px;top:14px"></div>
  <h2 class="title a center" style="top:18px">Analyse <span class="navy-t">Chart</span></h2>
  <p class="a" style="left:40px;top:75px;font-size:4.2px;font-weight:700">Finding Chart</p>
  <svg class="a" style="left:40px;top:96px" width="140" height="110" viewBox="0 0 140 110">
    <g font-size="3.8" fill="#555" text-anchor="end" font-family="Open Sans,sans-serif">
      <text x="47" y="15">Data Five</text><text x="47" y="33">Data Four</text><text x="47" y="51">Data Three</text><text x="47" y="69">Data Two</text><text x="47" y="87">Data One</text>
    </g>
    <line x1="52" y1="4" x2="52" y2="92" stroke="#ddd" stroke-width=".5"/>
    <line x1="116" y1="4" x2="116" y2="92" stroke="#eee" stroke-width=".5"/>
    <rect x="53" y="11" width="20" height="5" fill="#8a94a6"/>
    <rect x="53" y="29" width="28" height="5" fill="#23272f"/>
    <rect x="53" y="47" width="46" height="5" fill="#c8102e"/>
    <rect x="53" y="65" width="53" height="5" fill="#a7b0c0"/>
    <rect x="53" y="83" width="60" height="5" fill="#9b0f1e"/>
    <g font-size="3.8" fill="#555" text-anchor="middle" font-family="Open Sans,sans-serif"><text x="53" y="102">0</text><text x="84" y="102">100</text><text x="115" y="102">200</text></g>
  </svg>
  <div class="card" style="left:198px;top:68px;width:218px;height:140px;padding:9px 10px 0 12px">
    <p class="step-head" style="font-size:3.8px">● Analyse One:</p><p class="body" style="margin-bottom:6px">Lorem ipsum dolor sit amet, consectetuer adipiscing elit. Maecenas porttitor congue massa. Fusce posuere, magna sed pulvinar ultricies, purus lectus malesuada libero, sit amet commodo magna eros quis urna.</p>
    <p class="step-head" style="font-size:3.8px">● Analyse Two:</p><p class="body" style="margin-bottom:6px">Lorem ipsum dolor sit amet, consectetuer adipiscing elit. Maecenas porttitor congue massa. Fusce posuere, magna sed pulvinar ultricies, purus lectus malesuada libero, sit amet commodo magna eros quis urna.</p>
    <p class="step-head" style="font-size:3.8px">● Analyse Three:</p><p class="body">Lorem ipsum dolor sit amet, consectetuer adipiscing elit. Maecenas porttitor congue massa. Fusce posuere, magna sed pulvinar ultricies, purus lectus malesuada libero, sit amet commodo magna eros quis urna.</p>
  </div>
  <div class="footer"><span class="brand-mark">HARBORLINE SYSTEMS</span><span class="f-site">harborlinesys.com</span><span class="f-page">page | 13</span></div>
</section>

<section class="slide" style="left:330px;top:598.5px">
  <div class="photo" style="left:279px;top:0;width:124px;height:68px;background:linear-gradient(135deg,#4a4a4a,#9c9c9c 55%,#5e5e5e)" role="img" aria-label="Photo of a businessman walking across a striped street"></div>
  <div class="photo" style="left:279px;top:73px;width:124px;height:145px;background:linear-gradient(160deg,#3a4e74,#1d2b4a 55%,#6c6f8c)" role="img" aria-label="Photo of a glass skyscraper facade at dusk"></div>
  <div class="accent" style="left:36px;top:46px"></div>
  <h2 class="a" style="left:36px;top:52px;font-size:12.5px;font-weight:600">Professional Plan</h2>
  <p class="body a" style="left:36px;top:76px;width:180px"><b style="color:var(--ink)">Lorem ipsum</b> dolor sit amet, consectetuer adipiscing elit. Maecenas porttitor congue massa. Fusce posuere, magna sed pulvinar ultricies.</p>
  <div class="a" style="left:43px;top:129px;width:70px"><p class="step-head">First Step</p><p class="body">Lorem ipsum dolor sit amet, consectetuerpisc. Maecenas port congue.</p></div>
  <div class="a" style="left:135px;top:129px;width:70px"><p class="step-head">Second Step</p><p class="body">Lorem ipsum dolor sit amet, consectetuerpisc. Maecenas port congue.</p></div>
  <div class="card" style="left:220px;top:122px;width:80px;height:55px;padding:7px 7px"><p class="step-head">Third Step</p><p class="body">Lorem ipsum dolor sit amet, consectetuerpisc. Maecenas port congue.</p></div>
  <div class="footer"><span class="brand-mark">HARBORLINE SYSTEMS</span><span class="f-site">harborlinesys.com</span><span class="f-page">page | 14</span></div>
</section>

<section class="slide" style="left:617.5px;top:598.5px">
  <div class="accent" style="left:24px;top:16px"></div>
  <h2 class="a" style="left:24px;top:20px;font-size:12px;font-weight:600">Business Strategy</h2>
  <div class="card fill" style="left:23px;top:51px;width:121px;height:73px;padding:14px 9px"><p style="font-size:4.4px;font-weight:700;margin-bottom:2px">Strategy Company One</p><div style="width:5px;height:1px;background:#fff;margin-bottom:6px"></div><p class="body">Lorem ipsum dolor sit amet, consectetuer adipiscing elit. Maece nas porttitor congue.</p></div>
  <div class="card" style="left:161px;top:51px;width:121px;height:73px;padding:14px 9px"><p style="font-size:4.4px;font-weight:700;margin-bottom:2px">Strategy Company Two</p><div class="dash" style="margin:0 0 6px"></div><p class="body">Lorem ipsum dolor sit amet, consectetuer adipiscing elit. Maece nas porttitor congue.</p></div>
  <div class="card" style="left:299px;top:51px;width:121px;height:73px;padding:14px 9px"><p style="font-size:4.4px;font-weight:700;margin-bottom:2px">Strategy Company Three</p><div class="dash" style="margin:0 0 6px"></div><p class="body">Lorem ipsum dolor sit amet, consectetuer adipiscing elit. Maecenas porttitor congue.</p></div>
  <div class="card" style="left:23px;top:138px;width:121px;height:73px;padding:14px 9px"><p style="font-size:4.4px;font-weight:700;margin-bottom:2px">Strategy Company Four</p><div class="dash" style="margin:0 0 6px"></div><p class="body">Lorem ipsum dolor sit amet, consectetuer adipiscing elit. Maecenas porttitor congue.</p></div>
  <div class="card" style="left:161px;top:138px;width:121px;height:73px;padding:14px 9px"><p style="font-size:4.4px;font-weight:700;margin-bottom:2px">Strategy Company Five</p><div class="dash" style="margin:0 0 6px"></div><p class="body">Lorem ipsum dolor sit amet, consectetuer adipiscing elit. Maecenas porttitor congue.</p></div>
  <div class="card" style="left:299px;top:138px;width:121px;height:73px;padding:14px 9px"><p style="font-size:4.4px;font-weight:700;margin-bottom:2px">Strategy Company Six</p><div class="dash" style="margin:0 0 6px"></div><p class="body">Lorem ipsum dolor sit amet, consectetuer adipiscing elit. Maecenas porttitor congue.</p></div>
  <svg class="a" style="left:0;top:0" width="447" height="248" viewBox="0 0 447 248"><g fill="none" stroke-width=".9">
    <circle cx="132" cy="63" r="3" stroke="#fff"/><path d="M266 61l4-2 4 2-4 2zM266 64l4 2 4-2" stroke="var(--navy)"/>
    <g stroke="var(--navy)"><rect x="404" y="59" width="3" height="3"/><rect x="409" y="59" width="3" height="3"/><rect x="404" y="64" width="3" height="3"/><rect x="409" y="64" width="3" height="3"/>
    <rect x="128" y="146" width="3" height="3"/><rect x="133" y="146" width="3" height="3"/><rect x="128" y="151" width="3" height="3"/><rect x="133" y="151" width="3" height="3"/>
    <circle cx="270" cy="150" r="3"/><circle cx="270" cy="150" r="1"/>
    <circle cx="404" cy="150" r="1.5"/><circle cx="410" cy="147" r="1.5"/><circle cx="410" cy="153" r="1.5"/><path d="M405 149l4-2M405 151l4 2"/></g>
  </g></svg>
  <div class="footer"><span class="brand-mark">HARBORLINE SYSTEMS</span><span class="f-site">harborlinesys.com</span><span class="f-page">page | 18</span></div>
</section>

<section class="slide" style="left:905px;top:598.5px">
  <div class="photo" style="left:0;top:0;width:165px;height:200px;background:linear-gradient(180deg,#fff,#dfe2e7 60%,#9aa1ad)" role="img" aria-label="Photo of a white glass tower seen from below"></div>
  <div class="accent" style="left:226px;top:34px"></div>
  <h2 class="a" style="left:226px;top:38px;font-size:12.5px;font-weight:600">Business Steps</h2>
  <p class="body a" style="left:226px;top:60px;width:175px"><b style="color:var(--ink)">Lorem ipsum</b> dolor sit amet, consectetuer adipiscing elit. Maecenas porttitor congue massa. Fusce posuere, magna sed pulvinar ultricies.</p>
  <svg class="a" style="left:0;top:0" width="447" height="248" viewBox="0 0 447 248"><g stroke="var(--navy)" stroke-width=".7" fill="var(--navy)">
    <line x1="165" y1="91" x2="213" y2="91"/><circle cx="214" cy="91" r="1.3"/>
    <line x1="165" y1="130" x2="232" y2="130"/><circle cx="233" cy="130" r="1.3"/>
    <line x1="165" y1="169" x2="250" y2="169"/><circle cx="251" cy="169" r="1.3"/></g></svg>
  <div class="a" style="left:224px;top:85px;width:150px"><p class="step-head" style="font-size:3.8px;font-weight:700">First Step</p><p class="body">Lorem ipsum dolor sit amet, consectetuer adipisc. Maecenas porttitor congue.</p></div>
  <div class="a" style="left:243px;top:124px;width:150px"><p class="step-head" style="font-size:3.8px;font-weight:700">Second Step</p><p class="body">Lorem ipsum dolor sit amet, consectetuer adipisc. Maecenas porttitor congue.</p></div>
  <div class="a" style="left:261px;top:163px;width:150px"><p class="step-head" style="font-size:3.8px;font-weight:700">Third Step</p><p class="body">Lorem ipsum dolor sit amet, consectetuer adipisc. Maecenas porttitor congue.</p></div>
  <div class="footer"><span class="brand-mark">HARBORLINE SYSTEMS</span><span class="f-site">harborlinesys.com</span><span class="f-page">page | 19</span></div>
</section>

<!-- Row 5 -->
<section class="slide" style="left:43px;top:785px">
  <div class="photo" style="left:0;top:42px;width:225px;height:158px;background:linear-gradient(135deg,#cdd6e2,#8fa3bb 50%,#3b475a)" role="img" aria-label="Photo of hands at a laptop on a bright office desk"></div>
  <div class="accent" style="left:247px;top:46px"></div>
  <h2 class="a" style="left:247px;top:50px;font-size:12.5px;font-weight:600">Business Plan</h2>
  <p class="body a" style="left:247px;top:72px;width:170px"><b style="color:var(--ink)">Lorem ipsum</b> dolor sit amet, consectetuer adipiscing elit. Maecenas porttitor congue massa fusce posuere.</p>
  <div class="a" style="left:247px;top:98px;width:170px"><p class="step-head" style="font-size:3.8px">■ First Plan</p><p class="body" style="padding-left:8px">• Lorem ipsum dolor sit amet, consectetuer adipisc.<br>• Lorem ipsum dolor sit amet, consectetuer adipisc.<br>• Lorem ipsum dolor sit amet, consectetuer adipisc.</p></div>
  <div class="a" style="left:247px;top:146px;width:170px"><p class="step-head" style="font-size:3.8px">■ Second Plan</p><p class="body" style="padding-left:8px">• Lorem ipsum dolor sit amet, consectetuer adipisc.<br>• Lorem ipsum dolor sit amet, consectetuer adipisc.<br>• Lorem ipsum dolor sit amet, consectetuer adipisc.</p></div>
  <div class="footer"><span class="brand-mark">HARBORLINE SYSTEMS</span><span class="f-site">harborlinesys.com</span><span class="f-page">page | 21</span></div>
</section>

<section class="slide" style="left:330px;top:785px">
  <h2 class="a" style="left:14px;top:6px;font-size:7.5px;font-weight:700">Gauge Data <span class="red">Elements</span></h2>
  <div class="card" style="left:14px;top:28px;width:208px;height:94px"></div>
  <div class="card" style="left:226px;top:28px;width:208px;height:94px"></div>
  <div class="card" style="left:14px;top:126px;width:208px;height:92px"></div>
  <div class="card" style="left:226px;top:126px;width:208px;height:92px"></div>
  <svg class="a" style="left:0;top:0" width="447" height="248" viewBox="0 0 447 248" font-family="Open Sans,sans-serif">
    <g font-size="3.8" font-weight="700" text-anchor="middle" fill="#333">
      <text x="73" y="38">Data Three</text><text x="175" y="38">Data Three</text>
      <text x="73" y="44" font-weight="400" fill="#777">0</text><text x="175" y="44" font-weight="400" fill="#777">0</text>
      <text x="101" y="134">Data Three</text><text x="202" y="134">Data Three</text>
      <text x="273" y="137">Gauge One</text><text x="373" y="137">Gauge Two</text>
    </g>
    <g fill="none" stroke-width="6">
      <path d="M55 75a18 18 0 0 1 36 0" stroke="#3b4455"/>
      <path d="M55 75a18 18 0 0 1 36 0" stroke="#c8102e" pathLength="100" stroke-dasharray="32 100" stroke-dashoffset="-38"/>
      <path d="M157 75a18 18 0 0 1 36 0" stroke="#3b4455"/>
      <path d="M157 75a18 18 0 0 1 36 0" stroke="#c8102e" pathLength="100" stroke-dasharray="20 100" stroke-dashoffset="-40"/>
    </g>
    <path d="M73 75l12-6" stroke="#1d3763" stroke-width="1.8"/><circle cx="73" cy="75" r="2" fill="#1d3763"/>
    <path d="M175 75l-5-9" stroke="#1d3763" stroke-width="1.8"/><circle cx="175" cy="75" r="2" fill="#1d3763"/>
    <g font-size="5" font-weight="700" text-anchor="middle" fill="#1d3763"><text x="73" y="88">68%</text><text x="175" y="88">-20%</text></g>
    <g fill="none">
      <circle cx="273" cy="70" r="18" stroke="#e6e8ee" stroke-width="1.5"/>
      <circle cx="273" cy="70" r="18" stroke="#5a4a6e" stroke-width="2" pathLength="100" stroke-dasharray="68 100" transform="rotate(-90 273 70)"/>
      <circle cx="373" cy="70" r="18" stroke="#e6e8ee" stroke-width="1.5" stroke-dasharray="1 1.5"/>
      <circle cx="373" cy="70" r="18" stroke="#c8102e" stroke-width="2" pathLength="100" stroke-dasharray="36 100" transform="rotate(-90 373 70)"/>
    </g>
    <g font-size="4.4" font-weight="700" text-anchor="middle" fill="#333"><text x="273" y="71">68%</text><text x="373" y="71">36%</text></g>
    <g font-size="2.4" text-anchor="middle" fill="#999"><text x="273" y="76">PROFIT PLAN</text><text x="373" y="76">PROFIT LOSS</text></g>
    <g fill="none" stroke-width="4" stroke-dasharray=".6 1.6">
      <circle cx="73" cy="180" r="17" stroke="#c8102e"/>
      <circle cx="175" cy="180" r="17" stroke="#3b4455"/>
    </g>
    <g font-size="4.4" font-weight="700" text-anchor="middle" fill="#333"><text x="73" y="182">64%</text><text x="175" y="182">23%</text></g>
    <g fill="none" stroke-width="4" stroke-dasharray=".6 1.4">
      <path d="M258 178a15 15 0 0 1 30 0" stroke="#3b4455"/>
      <path d="M358 178a15 15 0 0 1 30 0" stroke="#c8102e"/>
    </g>
    <path d="M273 178l7-8" stroke="#1d3763" stroke-width="1.6"/><circle cx="273" cy="178" r="1.8" fill="#1d3763"/>
    <path d="M373 178l-8-5" stroke="#1d3763" stroke-width="1.6"/><circle cx="373" cy="178" r="1.8" fill="#1d3763"/>
    <g font-size="4.6" font-weight="700" text-anchor="middle" fill="#333"><text x="273" y="196">+32</text><text x="373" y="196">-75</text></g>
  </svg>
  <div class="footer"><span class="brand-mark">HARBORLINE SYSTEMS</span><span class="f-site">harborlinesys.com</span><span class="f-page">page | 22</span></div>
</section>

<section class="slide" style="left:617.5px;top:785px">
  <h2 class="a dash-title" style="left:14px;top:6px">Data Element <span class="red">Dashboard</span></h2>
  <div class="card" style="left:19px;top:42px;width:76px;height:68px;padding-top:7px"><p class="kpi-label">Data One</p><p class="kpi" style="margin-top:4px">10,889</p><p class="kpi-label" style="font-size:2.6px">Number</p><p class="kpi-label" style="margin-top:5px;font-size:3px"><span class="red">▲</span> 4 %</p></div>
  <div class="card" style="left:102px;top:42px;width:76px;height:68px;padding-top:7px"><p class="kpi-label">Data Two</p><p class="kpi red" style="margin-top:4px">12,455</p><p class="kpi-label" style="font-size:2.6px">Number</p><p class="kpi-label" style="margin-top:5px;font-size:3px"><span class="red">▲</span> 3 %</p></div>
  <div class="card" style="left:185px;top:42px;width:76px;height:68px;padding-top:7px"><p class="kpi-label">Data Three</p><p class="kpi" style="margin-top:4px">$59K</p><p class="kpi-label" style="font-size:2.6px">Number</p><p class="kpi-label" style="margin-top:5px;font-size:3px"><span class="red">▲</span> 11 %</p></div>
  <div class="card" style="left:268px;top:42px;width:76px;height:68px;padding-top:7px"><p class="kpi-label">Data Four</p><p class="kpi red" style="margin-top:4px">89%</p><p class="kpi-label" style="font-size:2.6px">Number</p><p class="kpi-label" style="margin-top:5px;font-size:3px"><span class="red">▼</span> 5 %</p></div>
  <div class="card" style="left:351px;top:42px;width:76px;height:68px;padding-top:7px"><p class="kpi-label">Data Five</p><p class="kpi" style="margin-top:4px">76K</p><p class="kpi-label" style="font-size:2.6px">Number</p><p class="kpi-label" style="margin-top:5px;font-size:3px"><span class="red">▲</span> 4 %</p></div>
  <div class="card" style="left:19px;top:118px;width:160px;height:94px"></div>
  <div class="card" style="left:185px;top:118px;width:160px;height:94px"></div>
  <div class="card" style="left:351px;top:118px;width:76px;height:94px;padding:10px 7px">
    <svg class="icon" width="14" height="12" viewBox="0 0 14 12"><g fill="none" stroke="var(--navy)" stroke-width=".8"><rect x="1" y="1" width="12" height="8"/><path d="M5 11h4M7 9v2M3 7l3-3 2 2 3-3"/></g></svg>
    <p class="kpi" style="font-size:5.5px;margin:4px 0 8px">100%</p>
    <p style="font-size:3.4px;font-weight:700">Working Hour</p><p class="body">Lorem Ipsum is not simply random text.</p>
  </div>
  <svg class="a" style="left:0;top:0" width="447" height="248" viewBox="0 0 447 248" font-family="Open Sans,sans-serif">
    <g font-size="3.4" font-weight="700" fill="#333" text-anchor="middle"><text x="99" y="128">Data One</text><text x="265" y="128">Data Two</text></g>
    <polygon points="30,204 45,198 60,200 75,190 90,194 105,182 120,186 135,170 150,176 165,148 168,204" fill="#dfe2e8"/>
    <polygon points="30,204 45,201 60,202 75,198 90,199 105,194 120,196 135,188 150,190 168,172 168,204" fill="var(--navy)"/>
    <g fill="var(--navy)"><circle cx="198" cy="200" r=".9"/><circle cx="214" cy="198" r=".9"/><circle cx="230" cy="199" r=".9"/><circle cx="246" cy="196" r=".9"/><circle cx="262" cy="197" r=".9"/><circle cx="278" cy="194" r=".9"/><circle cx="294" cy="192" r=".9"/><circle cx="310" cy="190" r=".9"/><circle cx="328" cy="185" r=".9"/></g>
    <polyline points="198,196 214,192 230,194 246,188 262,186 278,188 294,178 310,172 328,150" fill="none" stroke="#c8102e" stroke-width=".6" stroke-dasharray="1.5 1.5"/>
    <g fill="#c8102e"><circle cx="198" cy="196" r=".9"/><circle cx="230" cy="194" r=".9"/><circle cx="262" cy="186" r=".9"/><circle cx="294" cy="178" r=".9"/><circle cx="328" cy="150" r=".9"/></g>
  </svg>
  <div class="footer"><span class="brand-mark">HARBORLINE SYSTEMS</span><span class="f-site">harborlinesys.com</span><span class="f-page">page | 23</span></div>
</section>

<section class="slide" style="left:905px;top:785px">
  <h2 class="a dash-title" style="left:14px;top:6px">Data Element <span class="red">Dashboard</span></h2>
  <div class="card" style="left:19px;top:30px;width:86px;height:53px;padding:8px 6px"><p style="font-size:6px;font-weight:600">$344K</p><div class="dash" style="margin:2px 0 4px"></div><p class="body" style="font-size:3px">Contrary to popular belief, Lorem Ipsum is not simply.</p></div>
  <div class="card" style="left:110px;top:30px;width:86px;height:53px;padding:8px 6px"><p style="font-size:6px;font-weight:600">76%</p><div class="dash" style="margin:2px 0 4px"></div><p class="body" style="font-size:3px">Contrary to popular belief, Lorem Ipsum is not simply.</p></div>
  <div class="card" style="left:201px;top:30px;width:86px;height:53px;padding:8px 6px"><p style="font-size:6px;font-weight:600">78Mb</p><div class="dash" style="margin:2px 0 4px"></div><p class="body" style="font-size:3px">Contrary to popular belief, Lorem Ipsum is not simply.</p></div>
  <div class="card" style="left:19px;top:90px;width:131px;height:53px"></div>
  <div class="card" style="left:156px;top:90px;width:131px;height:53px"></div>
  <div class="a" style="left:82px;top:103px;width:60px"><p style="font-size:5px;font-weight:600">August</p><p class="body" style="font-size:3px">Contrary to popular belief, Lorem Ipsum is not.</p></div>
  <div class="a" style="left:219px;top:103px;width:60px"><p style="font-size:5px;font-weight:600">September</p><p class="body" style="font-size:3px">Contrary to popular belief, Lorem Ipsum is not.</p></div>
  <div class="card" style="left:307px;top:30px;width:121px;height:188px;padding:10px 8px 0 14px">
    <p style="font-size:4.4px;font-weight:600;text-align:center;margin-bottom:6px">Step Way</p>
    <p style="font-size:3.2px;font-weight:700">Lorem Ipsum One</p><p class="body" style="font-size:3px;margin-bottom:8px">Contrary to popular belief, Lorem Ipsum is not simply random text. It has roots in a piece of classical.</p>
    <p style="font-size:3.2px;font-weight:700">Lorem Ipsum One</p><p class="body" style="font-size:3px;margin-bottom:12px">It is a long established fact that a reader will be distracted by the readable content of a page when looking at its layout. Contrary to popular belief, Lorem Ipsum is not simply random text.</p>
    <p style="font-size:3.6px;font-weight:600">Revise Evaluation</p><p style="font-size:3.2px;font-weight:700;margin-top:6px">Lorem Ipsum One</p><p class="body" style="font-size:3px">45% - 79%</p>
  </div>
  <svg class="a" style="left:0;top:0" width="447" height="248" viewBox="0 0 447 248" font-family="Open Sans,sans-serif">
    <g fill="none" stroke-width="3.5">
      <circle cx="48" cy="116" r="11" stroke="#e4e7ee"/><circle cx="48" cy="116" r="11" stroke="var(--navy)" pathLength="100" stroke-dasharray="35 100" transform="rotate(-90 48 116)"/>
      <circle cx="185" cy="116" r="11" stroke="#e4e7ee"/><circle cx="185" cy="116" r="11" stroke="var(--navy)" pathLength="100" stroke-dasharray="63 100" transform="rotate(-90 185 116)"/>
    </g>
    <g font-size="3.6" font-weight="700" text-anchor="middle" fill="#333"><text x="48" y="117.5">35%</text><text x="185" y="117.5">63%</text></g>
    <g fill="none" stroke="#c7ccd6" stroke-width=".5"><circle cx="316" cy="43" r="2"/><circle cx="316" cy="84" r="2"/><circle cx="316" cy="106" r="2"/><circle cx="316" cy="176" r="2"/><circle cx="316" cy="198" r="2"/><line x1="316" y1="45" x2="316" y2="196"/></g>
    <polygon points="50,218 80,216 110,214 140,210 160,206 175,190 185,163 192,172 198,168 206,186 218,200 240,208 270,214 290,216 290,218" fill="var(--navy)"/>
    <polyline points="50,216 80,214 110,212 140,208 160,204 175,186 185,160 192,170 198,164 206,184 218,196 240,206 270,212 290,214" fill="none" stroke="#c8102e" stroke-width=".6"/>
  </svg>
  <div class="footer"><span class="brand-mark">HARBORLINE SYSTEMS</span><span class="f-site">harborlinesys.com</span><span class="f-page">page | 24</span></div>
</section>

</body>
</html>
```